Looking for an Innovative Print Design (Service Directory)

We need a new design for our advertisement within a printed colour services directory.

We are a compensation law firm called Velbrook Compensation Lawyers. Feel free to take a browse of our website www.velbrooklegal.com.au to get an idea of what we do and the kind of firm we are.

We are in the process of redeveloping our website and as such, so please don't adhere to the design principles of the current site- impress us with your originality!

On top of any editable formats, your final submissions must include a .pdf copy.
The same design will need to be presented in two dimensions:

- 154mm x 118mm (B1/B2 Half Page);
- 175mm x 113mm (B4 Half Page).

[For more information refer to attached Pdf.]

We have attached for you a few examples of other firms' designs (Sample1,2,3). These are by no means good, or what we're after, it's just to provide you with an idea of what sort of advertisements go into the service directory.

Hi all,

We want to emphasise that a priority of the design is that it must look:
• Professional
• Sophisticated
Please do not hesitate to use completely different colour schemes to the ones that are on our website- as we have said, our website will change in the near future, so cohesion between the current project and the website is not necessary!

Thanks!

Thank you for your submissions so far. There are some great ideas hidden in there. 

An issue we are having is that most of you are conforming to the same understanding of what it should look like. Remember that there is NO NEED to be bound by the image of firm as is. That is, feel free to use a different colour logo.

For inspiration, we relate well to the design aesthetics of: http://www.tinfernstudio.co.uk/

Look forward to seeing your 'out of the box' submissions. 

Reason: We've received a large amount of fantastic designs. However, what we're really looking for is something original. Please feel free to think outside the box (the final design doesn't need to look like a print ad), and construct a design that is completely incongruous with our website! While we do appreciate a minimalistic design, we have yet to receive something that really grabs your attention with its visuals. We're not sure but this may or may not be achieved with a full colour design. Thanks for all your submissions- they all have some features that really click with us. We look forward to the next wave of submissions!

Target Market(s)

We have various target markets, including mainly families, elderly people, blue collar workers.

These are individuals who are looking for assistance. They feel helpless or wronged.

Keep in mind that the people accessing these are those who prefer going to a printed directory rather than using a google search.

Industry/Entity Type

Law Firm

Font styles to use
Serif
Sans Serif

Requirements
Must have
• - Our name 'Velbrook Compensation Lawyers'
- Our logo (attached as logo.eps, logo.png, and logo.tif)
- Must include phone number as 1300 XXX XXX (this must be prominent)
- Must include the following service areas in these words: Motor vehicle claims, medical claims, superannuation claims, Workplace claims, negligence claims
- Our email address: info@velbrooklegal.com.au
- Our website address: www.velbrooklegal.com.au
- The following catchphrases: '98% success rate', and 'No win no fee' in those words
- Our location '412 Carvel Lane, Smithville, SYDNEY'
- For sizing dimensions, we need one in 154mm x 118mm and also a design in 175mm x 113mm (B4 Half Page) [refer to pdf attached]
Nice to have
• - Text indicating free initial consulatation
- Professional colour scheme
- As our website will be changed, do not worry about making the advertisement cohesive with our website design
- We want the design to be modern, but still professional
- Clean typeface
- No gradient colour scheme
- When designing, if you are looking to place more text onto the advertisement, these may be some considerations (feel free to change the wording): Accredited specialists, home and hospital visits

```html
<!DOCTYPE html>
<html lang="en">
<head>
<meta charset="utf-8">
<title>Velbrook Compensation Lawyers – Directory Advertisement</title>
<link rel="stylesheet" href="https://fonts.googleapis.com/css2?family=Montserrat:wght@300;500;600;700&family=Great+Vibes&display=swap">
<style>
  :root {
    --sky-deep: #2a64a8;
    --sky-mid: #4a86c6;
    --sky-soft: #7eaad8;
    --ink-blue: #2c6aa6;
    --ink-navy: #1d4f7e;
    --accent-orange: #d5692c;
    --white: #ffffff;
    --band-dark: #1c4a73;
  }
  * { margin: 0; padding: 0; box-sizing: border-box; }
  html, body { width: 1200px; height: 920px; overflow: hidden; background: var(--white); }
  .ad {
    position: relative;
    width: 1200px;
    height: 920px;
    overflow: hidden;
    font-family: "Montserrat", Arial, sans-serif;
    background: var(--white);
  }
  .sky-photo {
    position: absolute;
    left: 0; top: 0;
    width: 1200px; height: 750px;
    background: linear-gradient(180deg, var(--sky-deep) 0%, var(--sky-mid) 60%, var(--sky-soft) 100%);
  }
  .stat-card {
    position: absolute;
    right: 0; top: 0;
    width: 362px; height: 296px;
    background: var(--white);
    clip-path: polygon(0 0, 100% 0, 100% 100%, 20px 100%, 0 calc(100% - 20px));
    color: var(--ink-blue);
    font-weight: 700;
    line-height: 0.86;
    padding: 34px 0 0 32px;
  }
  .stat-card .figure { font-size: 106px; letter-spacing: -2px; display: block; }
  .stat-card .label { font-size: 57px; letter-spacing: -1px; display: block; margin-top: 2px; }
  .stat-card .label-big { font-size: 114px; letter-spacing: -3px; display: block; margin-top: -4px; }

  .brand {
    position: absolute;
    left: 335px; top: 398px;
    display: flex;
    align-items: center;
    gap: 40px;
    color: var(--white);
  }
  .brand-dot {
    width: 134px; height: 134px;
    border-radius: 50%;
    background: var(--accent-orange);
    flex: none;
  }
  .brand-name .primary { display: block; font-size: 74px; font-weight: 300; letter-spacing: 4px; line-height: 1; }
  .brand-name .secondary { display: block; font-size: 21px; font-weight: 600; letter-spacing: 3.6px; margin-top: 14px; }

  .tagline {
    position: absolute;
    left: 762px; top: 518px;
    font-family: "Great Vibes", cursive;
    font-size: 66px;
    color: var(--white);
  }
  .services {
    position: absolute;
    left: 0; top: 650px;
    width: 1200px;
    text-align: center;
    color: var(--white);
    font-weight: 700;
    font-size: 29px;
    line-height: 44px;
  }
  .contact-bar {
    position: absolute;
    left: 0; top: 750px;
    width: 1200px; height: 122px;
    background: var(--white);
  }
  .address {
    position: absolute;
    left: 40px; top: 22px;
    font-size: 30px;
    font-weight: 700;
    letter-spacing: 0.6px;
    color: var(--ink-blue);
  }
  .divider {
    position: absolute;
    left: 725px; top: 8px;
    width: 1px; height: 98px;
    background: var(--ink-navy);
  }
  .contact-list {
    position: absolute;
    left: 793px; top: 10px;
    list-style: none;
    color: var(--ink-navy);
    font-weight: 600;
    font-size: 20px;
    letter-spacing: 1.6px;
    line-height: 29px;
  }
  .contact-list .phone {
    display: flex;
    align-items: center;
    gap: 16px;
    font-size: 29px;
    font-weight: 700;
    letter-spacing: 0;
    margin-top: 4px;
  }
  .footer-band {
    position: absolute;
    left: 0; top: 872px;
    width: 1200px; height: 18px;
    background: linear-gradient(90deg, var(--band-dark), var(--ink-blue), var(--band-dark));
  }
</style>
</head>
<body>
<div class="ad">
  <div class="sky-photo" role="img" aria-label="Photograph of a bright blue sky with white clouds and sun rays breaking through"></div>

  <div class="stat-card">
    <span class="figure">98%</span>
    <span class="label">success</span>
    <span class="label-big">rate</span>
  </div>

  <div class="brand">
    <span class="brand-dot"></span>
    <div class="brand-name">
      <span class="primary">VELBROOK</span>
      <span class="secondary">COMPENSATION LAWYERS</span>
    </div>
  </div>

  <p class="tagline">No win no fee</p>

  <p class="services">
    Motor vehicle claims, medical claims, superannuation claims,<br>
    Workplace claims, negligence claims
  </p>

  <div class="contact-bar">
    <p class="address">412 Carvel Lane, Smithville, SYDNEY</p>
    <span class="divider"></span>
    <ul class="contact-list">
      <li>www.velbrooklegal.com.au</li>
      <li>info@velbrooklegal.com.au</li>
      <li class="phone">
        <svg width="30" height="24" viewBox="0 0 30 24" aria-hidden="true">
          <path d="M3 8 Q15 0 27 8 L25 11 L20 10 L19 7 Q15 5.5 11 7 L10 10 L5 11 Z" fill="none" stroke="#1d4f7e" stroke-width="1.6"/>
          <rect x="6" y="12" width="18" height="10" rx="2" fill="none" stroke="#1d4f7e" stroke-width="1.6"/>
          <circle cx="15" cy="17" r="2.4" fill="#1d4f7e"/>
        </svg>
        1300 XXX XXX
      </li>
    </ul>
  </div>

  <div class="footer-band"></div>
</div>
</body>
</html>
```